Disability provider requiring digital flyer to promote services

My company works within the Disability sector (QCWP registered provider), currently operating in Sydney, Australia.
I require a digital brochure which lists our services and gives potential customers a quick look into what we do with a single glance.
Undecided whether this digital flyer is to be single or double sided, happy to consult with an experienced designer in this regard.
I prefer minimalist designs (which may be an issue for someone trying to convey information, I'm not sure), and possibly someone who can work with out watercolor logo.
Services include:
-Supported Independent Living
-Specialist Disability Accommodation
-Individualised Living Options Stage 1 & 2
-Home Modifications
-Occupational Therapy
-Support Coordination Levels 1 & 2
-Short Term Accommodation - STA Respite
-Drop In Supports
-Community Access

```html
<!DOCTYPE html>
<html lang="en">
<head>
<meta charset="utf-8">
<title>Our Services – Sunvale Healthcare</title>
<link href="https://fonts.googleapis.com/css2?family=Antonio:wght@200;300&family=Questrial&display=swap" rel="stylesheet">
<style>
  :root {
    --ink: #1c1f22;
    --text: #2f3438;
    --footer: #2e3338;
    --white: #ffffff;
    --mint: #7fe6bf;
    --violet: #a424ee;
    --orange: #f0a65c;
    --lilac: #c27cf0;
    --magenta: #d424e4;
    --teal: #52c2a2;
    --rose: #e6307e;
    --indigo: #5a56f0;
    --charcoal: #2f3438;
    --badge: #5a10c8;
    --brand: #2f3438;
  }
  * { box-sizing: border-box; margin: 0; padding: 0; }
  html, body { width: 927px; height: 1200px; overflow: hidden; background: var(--white); }
  .flyer {
    position: relative;
    width: 927px;
    height: 1200px;
    background: var(--white);
    font-family: "Questrial", "Century Gothic", sans-serif;
    color: var(--text);
  }
  .title {
    position: absolute;
    left: 60px;
    top: 52px;
    font-family: "Antonio", "Oswald", sans-serif;
    font-weight: 200;
    font-size: 96px;
    line-height: 1;
    letter-spacing: 1px;
    color: var(--ink);
  }
  .hero-art {
    position: absolute;
    right: 0;
    top: 0;
    width: 235px;
    height: 392px;
    background: radial-gradient(ellipse at 70% 25%, #f050e0 0%, #e070f0 35%, rgba(236,140,244,0.35) 65%, rgba(255,255,255,0) 80%),
                linear-gradient(180deg, rgba(255,255,255,0) 60%, rgba(170,200,240,0.35) 100%);
  }
  .services { list-style: none; }
  .service {
    position: absolute;
    left: 60px;
    display: flex;
    align-items: center;
    height: 55px;
  }
  .service-num {
    width: 55px;
    height: 55px;
    border-radius: 50%;
    color: var(--white);
    font-size: 25px;
    display: flex;
    align-items: center;
    justify-content: center;
    flex-shrink: 0;
  }
  .service-name {
    margin-left: 32px;
    font-size: 29.5px;
    white-space: nowrap;
    color: var(--text);
  }
  .contact {
    position: absolute;
    left: 60px;
    top: 968px;
    font-size: 28px;
    line-height: 40px;
    color: var(--text);
  }
  .partner-badge {
    position: absolute;
    left: 584px;
    top: 982px;
    width: 58px;
    height: 58px;
    border-radius: 50%;
    background: var(--badge);
  }
  .brand {
    position: absolute;
    left: 663px;
    top: 986px;
    font-size: 34px;
    line-height: 1.1;
    color: var(--brand);
    white-space: nowrap;
  }
  .footer {
    position: absolute;
    left: 0;
    top: 1071px;
    width: 927px;
    height: 129px;
    background: var(--footer);
    display: flex;
    align-items: center;
    justify-content: center;
    color: var(--white);
    font-size: 24.5px;
    padding-bottom: 6px;
  }
  .footer .dot { margin: 0 14px; }
</style>
</head>
<body>
<main class="flyer">
  <h1 class="title">OUR SERVICES:</h1>
  <div class="hero-art" role="img" aria-label="Watercolour pink and purple tree with a rope swing and butterflies"></div>

  <ol class="services">
    <li class="service" style="top:195px"><span class="service-num" style="background:var(--mint)">1.</span><span class="service-name">Supported Independent Living</span></li>
    <li class="service" style="top:277px"><span class="service-num" style="background:var(--violet)">2.</span><span class="service-name">Specialist Disability Accommodation</span></li>
    <li class="service" style="top:359px"><span class="service-num" style="background:var(--orange)">3.</span><span class="service-name">Individualised Living Options Stage 1 &amp; 2</span></li>
    <li class="service" style="top:441px"><span class="service-num" style="background:var(--lilac)">4.</span><span class="service-name">Home Modifications</span></li>
    <li class="service" style="top:524px"><span class="service-num" style="background:var(--magenta)">5.</span><span class="service-name">Occupational Therapy</span></li>
    <li class="service" style="top:606px"><span class="service-num" style="background:var(--teal)">6.</span><span class="service-name">Support Coordination Levels 1 &amp; 2</span></li>
    <li class="service" style="top:688px"><span class="service-num" style="background:var(--rose)">7.</span><span class="service-name">Short Term Accommodation - STA Respite</span></li>
    <li class="service" style="top:770px"><span class="service-num" style="background:var(--indigo)">8.</span><span class="service-name">Drop In Supports</span></li>
    <li class="service" style="top:853px"><span class="service-num" style="background:var(--charcoal)">9.</span><span class="service-name">Community Access</span></li>
  </ol>

  <p class="contact">Call 0400 318 562 For More Info!<br>9am To 5pm Monday To Friday</p>

  <div class="partner-badge" aria-hidden="true"></div>
  <p class="brand">Sunvale<br>Healthcare</p>

  <footer class="footer">
    <span>sunvalehealthcare.com.au</span><span class="dot">•</span><span>info@sunvalehealthcare.com.au</span>
  </footer>
</main>
</body>
</html>
```